Sports Performance Facility Grand Opening

I am planning the grand opening of my new training facility. We are moving and expanding. We specialize in training athletes of all ages and now will offer facility rentals. We will offer team training, group speed and agility training, baseball/softball academy, and our Football Academy. We would like to kick off our new Facility January 10th from 11:00-3:00pm. We will offer premium training packages and special facility rental rates at the opening. Along with this, if a team contacts us before the opening and mentions the post card, they will receive a special offer to rent the facility. We are going to relocate to 42 Corvell St just off I78 and conveniently located in the Lehigh Valley. We want to signify that we will provide elite training programs at a premium. Along with this, our facility rentals provide a unique opportunity for us to have a one stop shop for all our clients individual and team training needs. We are excited to get back into the Lehigh Valley and continue working with the Valley's premier teams and athletes. Provide tel #610.482.9067 and email. Marcus@marcuselwinpeak.com

Target Market(s)

We are targeting athletes ranging from youth levels to the professionals. youth, travel, and high school teams to rent our facility. Adults looking to workout like an athlete.

Industry/Entity Type

Training

Requirements
Must have
• Grand Opening and Special Offer/ Contact us to reserve our facility today.
Nice to have
• Be creative and create an idea that would cause people to bring friends/coaches/ etc...to receive additional program savings
Should not have
• Clip art that is old and outdated.

```html
<!DOCTYPE html>
<html lang="en">
<head>
<meta charset="utf-8">
<title>Grand Opening Postcard</title>
<link rel="stylesheet" href="https://fonts.googleapis.com/css2?family=Rubik+Dirt&family=Oswald:wght@600;700&family=Lato:wght@400;700;900&display=swap">
<style>
  :root{
    --bg:#e6e6e6;
    --black:#0b0b0b;
    --yellow:#f2b312;
    --gold:#f5b400;
    --red:#d4202a;
    --white:#ffffff;
    --ink:#2a2a2a;
    --line:#333333;
  }
  *{margin:0;padding:0;box-sizing:border-box}
  html,body{width:900px;height:1200px;overflow:hidden;background:var(--bg)}
  .canvas{position:relative;width:900px;height:1200px}

  /* ---------- Front ---------- */
  .card-front{position:absolute;left:110px;top:60px;width:662px;height:510px;background:var(--black)}
  .front-accent-top{position:absolute;left:-2px;top:-16px;width:250px;height:16px;background:var(--yellow);clip-path:polygon(0 0,90% 0,100% 100%,0 100%)}
  .front-accent-bottom{position:absolute;right:0;bottom:-14px;width:210px;height:28px;background:var(--yellow);clip-path:polygon(10% 0,100% 0,100% 100%,18% 100%)}
  .front-photo{position:absolute;left:28px;top:22px;width:604px;height:466px;
    background:linear-gradient(180deg,#5c5852 0%,#4a4744 45%,#4d6a35 70%,#3e5a2c 100%)}
  .front-shade{position:absolute;left:28px;top:22px;width:330px;height:466px;
    background:linear-gradient(90deg,rgba(0,0,0,.55),rgba(0,0,0,.25));clip-path:polygon(0 0,78% 0,100% 100%,0 100%)}
  .front-copy{position:absolute;left:44px;top:64px;width:320px}
  .headline{font-family:"Rubik Dirt",system-ui,sans-serif;color:var(--yellow);font-size:66px;line-height:64px;letter-spacing:1px;text-shadow:2px 2px 0 #000}
  .date{font-family:"Rubik Dirt",system-ui,sans-serif;color:var(--white);font-size:34px;line-height:34px;margin-top:26px;text-shadow:2px 2px 0 #000}
  .time{font-family:"Rubik Dirt",system-ui,sans-serif;color:var(--white);font-size:26px;line-height:30px;text-shadow:2px 2px 0 #000}
  .packages{font-family:"Oswald",sans-serif;font-weight:700;color:var(--red);font-size:20px;margin-top:34px;letter-spacing:.2px;text-shadow:1px 1px 0 #000}
  .rates{font-family:"Oswald",sans-serif;font-weight:700;color:var(--yellow);font-size:40px;line-height:40px;margin-top:10px;text-transform:uppercase;text-shadow:2px 2px 0 #000}
  .brand-box{position:absolute;left:378px;top:375px;width:284px;height:100px;background:var(--white);
    clip-path:polygon(0 0,100% 0,100% 100%,14% 100%);display:flex;flex-direction:column;align-items:center;justify-content:center;padding-left:36px}
  .brand-name{font-family:"Lato",sans-serif;font-weight:900;font-size:30px;color:var(--ink);letter-spacing:2px}
  .brand-tag{font-family:"Lato",sans-serif;font-weight:400;font-size:8.5px;color:var(--ink);margin-top:6px}

  /* ---------- Back ---------- */
  .card-back{position:absolute;left:110px;top:635px;width:662px;height:510px;background:var(--white)}
  .back-accent-top{position:absolute;left:-2px;top:-16px;width:230px;height:16px;background:var(--yellow);clip-path:polygon(0 0,88% 0,100% 100%,0 100%)}
  .back-accent-bottom{position:absolute;right:0;bottom:-14px;width:200px;height:30px;background:var(--yellow);clip-path:polygon(8% 0,100% 0,100% 100%,14% 100%)}
  .offer-panel{position:absolute;left:14px;top:15px;width:304px;height:481px;background:var(--black);overflow:hidden}
  .offer-photo{position:absolute;inset:0;background:linear-gradient(160deg,#1a1a1a 0%,#3a3532 45%,#262320 70%,#141414 100%);opacity:.9}
  .offer-copy{position:relative;padding:36px 20px 0 40px;color:var(--white);font-family:"Lato",sans-serif}
  .section-title{font-family:"Oswald",sans-serif;font-weight:700;color:var(--gold);font-size:26px;line-height:28px}
  .offer-list{list-style:none;margin-top:4px}
  .offer-list li{position:relative;padding-left:18px;font-size:19px;line-height:24px}
  .offer-list li::before{content:"";position:absolute;left:2px;top:9px;width:7px;height:7px;border-radius:50%;background:var(--red)}
  .promo{color:var(--red);font-weight:900;font-size:13.5px;line-height:15px;margin:8px 0 0 -2px}
  .section-title.small{font-size:17px;margin-top:28px;margin-left:-2px}
  .address{font-size:14.5px;line-height:16px;margin:6px 0 0 24px}
  .address small{font-size:12.5px}
  .contact-band{position:absolute;left:0;bottom:0;width:100%;height:82px;background:var(--gold);padding:14px 0 0 40px;font-family:"Lato",sans-serif;font-weight:700;font-size:14px;color:var(--ink)}
  .contact-row{display:flex;align-items:center;gap:8px;height:22px}
  .stamp-box{position:absolute;left:517px;top:73px;width:80px;height:88px;border:1px solid #555}
  .address-line{position:absolute;left:360px;width:236px;height:2px;background:var(--line)}
</style>
</head>
<body>
<div class="canvas">

  <section class="card-front">
    <div class="front-accent-top"></div>
    <div class="front-accent-bottom"></div>
    <div class="front-photo" role="img" aria-label="Photo of a football player in black and gold running with the ball on the field, crowd behind"></div>
    <div class="front-shade"></div>
    <div class="front-copy">
      <h1 class="headline">GRAND<br>OPENING</h1>
      <p class="date">JANUARY 10TH</p>
      <p class="time">FROM 11:00-3:00PM</p>
      <p class="packages">PREMIUM TRAINING PACKAGES</p>
      <p class="rates">Special Facility<br>Rental Rates</p>
    </div>
    <div class="brand-box">
      <div class="brand-name">PEAKFORM</div>
      <div class="brand-tag">Performance·Speed·Strength·Training</div>
    </div>
  </section>

  <section class="card-back">
    <div class="back-accent-top"></div>
    <div class="back-accent-bottom"></div>
    <div class="offer-panel">
      <div class="offer-photo" role="img" aria-label="Dark photo of football players in action"></div>
      <div class="offer-copy">
        <h2 class="section-title">WE OFFER</h2>
        <ul class="offer-list">
          <li>Team training</li>
          <li>Group speed</li>
          <li>Agility training</li>
          <li>Baseball/softball Academy</li>
          <li>Football Academy</li>
        </ul>
        <p class="promo">If a team contacts us before the opening and mentions the post card, they will receive a special offer to rent the facility.</p>
        <h3 class="section-title small">WE ARE TO RELOCATE TO</h3>
        <p class="address">42 Corvell St just off I78 and<br><small>conveniently located in the Lehigh Valley</small></p>
      </div>
      <div class="contact-band">
        <div class="contact-row">
          <svg width="12" height="12" viewBox="0 0 24 24" aria-hidden="true"><path fill="#2a2a2a" d="M6.6 10.8a15 15 0 0 0 6.6 6.6l2.2-2.2a1 1 0 0 1 1-.25 11.4 11.4 0 0 0 3.6.57 1 1 0 0 1 1 1V20a1 1 0 0 1-1 1A17 17 0 0 1 3 4a1 1 0 0 1 1-1h3.5a1 1 0 0 1 1 1c0 1.25.2 2.45.57 3.57a1 1 0 0 1-.25 1z"/></svg>
          <span>610.482.9067</span>
        </div>
        <div class="contact-row">
          <svg width="12" height="12" viewBox="0 0 24 24" aria-hidden="true"><circle cx="12" cy="12" r="10" fill="none" stroke="#2a2a2a" stroke-width="2.4"/><path d="M2 12h20M12 2c3 3 3 17 0 20M12 2c-3 3-3 17 0 20" fill="none" stroke="#2a2a2a" stroke-width="2"/></svg>
          <span>Marcus@marcuselwinpeak.com</span>
        </div>
      </div>
    </div>
    <div class="stamp-box"></div>
    <div class="address-line" style="top:252px"></div>
    <div class="address-line" style="top:292px"></div>
    <div class="address-line" style="top:332px"></div>
  </section>

</div>
</body>
</html>
```